Consulting Engineering Firm WordPress Design

We need:
1. A WordPress design.
2. Company is based in Sydney, Australia.
3. Company name: K7R Consulting Engineers.
The company provide professional engineering consultancy services to building owners, operators, developers and designers.
4. Overall purpose or objective of the website: The website must reflect high professionalism. It will provide information to our clients on who we are, what we do, how we do, our experience, projects we have done in the past and contact information.
5. Company logo is in the uploaded files.
6. Webpage:
6.1. Standard Web pages. Not for e-commercial.
6.2. Use WordPress. Website will be hosted on Hostvane WordPress hosting.
7. Coding required.
8. The winning designer (Winner) shall assist to host the wordpress design on Hostvane WordPress hosting services. Winner will transfer the files and configure to make sure all pages, links, posts and blogs works as intended.
8. We would like the site to have the same theme as the company brochure which is uploaded here.
9. The SSL certificate must be configured in the coded WordPress.
10. Pages:
i. Home - will have images updating every 4 s. Refer to company brochure for the images I am after. Use similar or better high quality images.
ii. About Us
iii. Services - This will have sub pages.
iv. Markets- This will have sub pages.
v. Projects- This will have sub pages.
vi. Contact - This will have company contact details. Also, it will request first name, last name, phone number, email address, comments and submit button.
11. I want a clean, minimalist websites that has a more professional tone. Please do not use too much unnecessary graphical elements and avoid loud vibrant colours.
12. Use images related to technology, buildings, smart city, smart buildings, energy savings, control system, energy dash boards, etc.
Target Market(s)
Building services engineering consultants, builders, building owners, building managers.

```html
<!DOCTYPE html>
<html lang="en">
<head>
<meta charset="utf-8">
<title>K7R Consulting Engineers</title>
<link href="https://fonts.googleapis.com/css2?family=Montserrat:wght@400;500;600;700;800&display=swap" rel="stylesheet">
<style>
:root{
  --blue:#0b5cab;
  --blue-light:#6fa9db;
  --navy:#0d2f5c;
  --navy-deep:#0c1b3a;
  --ink:#1b1b1b;
  --grey:#555c66;
  --pale:#eef2f7;
  --field:#e4e4e4;
  --white:#ffffff;
}
*{margin:0;padding:0;box-sizing:border-box}
html,body{width:1200px;height:4277px;overflow:hidden}
body{font-family:'Montserrat',sans-serif;color:var(--ink);background:var(--white);position:relative}
.abs{position:absolute}
a{color:inherit;text-decoration:none}

/* header */
.site-header{position:absolute;left:0;top:0;width:1200px;height:70px;background:var(--white);box-shadow:0 1px 4px rgba(0,0,0,.08);z-index:5}
.brand{position:absolute;left:150px;top:14px;display:flex;align-items:center;gap:8px}
.brand-dot{width:40px;height:40px;border-radius:50%;background:var(--blue)}
.brand-name{font-weight:800;font-size:15px;color:var(--blue);line-height:1.1}
.brand-name small{display:block;font-size:8px;font-weight:800;letter-spacing:.3px}
.main-nav{position:absolute;left:426px;top:27px;display:flex;gap:32px;font-size:13px;font-weight:500;color:#333}
.nav-cta{position:absolute;left:912px;top:18px;width:138px;height:37px;border-radius:20px;background:var(--blue);color:var(--white);font-size:13px;font-weight:600;display:flex;align-items:center;justify-content:center}

/* hero */
.hero{position:absolute;left:0;top:70px;width:1200px;height:730px;overflow:hidden}
.hero-photo{position:absolute;inset:0;background:linear-gradient(180deg,#2b3d52 0%,#3e5068 45%,#26374c 100%)}
.hero-feature{position:absolute;left:600px;top:62px;width:450px;height:450px;border-radius:40px;background:linear-gradient(160deg,#7b8ee0 0%,#3a5a9e 50%,#1c2d50 100%);opacity:.85}
.hero-kicker{position:absolute;left:146px;top:227px;color:var(--white);font-weight:600;font-size:18px}
.hero-title{position:absolute;left:146px;top:258px;color:var(--white);font-weight:800;font-size:74px;line-height:1}
.hero-sub{position:absolute;left:146px;top:350px;color:var(--white);font-weight:600;font-size:34px}
.hero-btn{position:absolute;left:150px;top:422px;width:165px;height:40px;border-radius:20px;background:var(--blue);color:var(--white);font-size:13px;font-weight:600;display:flex;align-items:center;padding-left:22px;gap:10px}
.hero-btn i{width:20px;height:20px;border-radius:50%;border:2px solid var(--white)}
.scroll-mouse{position:absolute;left:591px;top:563px;width:17px;height:30px;border:2px solid rgba(255,255,255,.6);border-radius:9px}
.hero-bands{position:absolute;left:0;top:0}

/* about */
.about{position:absolute;left:0;top:800px;width:1200px;height:562px;background:linear-gradient(180deg,#f5f7fb 0%,#e8edf3 100%)}
.about-visual{position:absolute;left:170px;top:65px;width:360px;height:390px;border-radius:180px 180px 30px 180px;background:linear-gradient(180deg,#8fb8e2 0%,#4d80b8 60%,#b9cde3 100%)}
.about-copy{position:absolute;left:646px;top:85px;width:380px}
.section-title{font-weight:400;font-size:37px;color:var(--ink)}
.section-title b{font-weight:800}
.about-copy p{font-size:13px;line-height:22px;color:#333;margin-top:16px}
.about-copy .first{margin-top:20px}
.text-link{display:inline-block;margin-top:22px;font-size:13px;color:var(--blue);text-decoration:underline}

.connector{position:absolute;left:599px;width:2px;border-left:2px dotted #555}
.connector:before{content:"";position:absolute;left:-6px;top:-9px;width:8px;height:8px;border:1.5px solid #555;border-radius:50%}
.connector:after{content:"";position:absolute;left:-5px;bottom:0;width:7px;height:7px;border-right:1.5px solid #555;border-bottom:1.5px solid #555;transform:rotate(45deg)}

/* intro cards */
.intro-card{position:absolute;top:1452px;width:277px;text-align:center}
.card-photo{width:277px;height:188px}
.card-badge{width:38px;height:38px;border-radius:50%;background:var(--white);border:2px solid var(--blue);margin:-22px auto 0;position:relative}
.card-badge:after{content:"";position:absolute;left:11px;top:11px;width:12px;height:12px;border-radius:50%;background:var(--blue)}
.intro-card h3{font-weight:500;font-size:19px;margin-top:4px}
.intro-card p{font-size:12px;line-height:19px;color:var(--grey);margin-top:10px}
.pill-btn{display:inline-flex;align-items:center;justify-content:center;margin-top:18px;width:122px;height:30px;border-radius:15px;background:var(--navy);color:var(--white);font-size:10px;font-weight:700;gap:6px}
.pill-btn:after{content:"";border-left:5px solid var(--white);border-top:3px solid transparent;border-bottom:3px solid transparent}

/* what we do */
.services{position:absolute;left:0;top:1880px;width:1200px;height:764px;background:linear-gradient(180deg,#0e4a8a 0%,#0c3d75 50%,#0f3f78 100%)}
.services-title{position:absolute;left:0;top:2062px;width:1200px;text-align:center;color:var(--white);font-size:40px;font-weight:400}
.services-title b{font-weight:800}
.services-lede{position:absolute;left:0;top:2120px;width:1200px;text-align:center;color:var(--white);font-size:17px}
.service-item{position:absolute;color:var(--white);font-weight:600;font-size:23px}
.service-hub{position:absolute;left:482px;top:2245px;width:236px;height:250px;border-radius:118px 118px 40px 40px;background:linear-gradient(180deg,#a9c9ec 0%,#4a78b1 60%,#1d3a66 100%)}

/* stats */
.stat{position:absolute;top:2698px;width:200px;text-align:center}
.stat-ring{width:70px;height:70px;margin:0 auto;border-radius:50%;border:3px solid var(--blue);border-right-color:#c9d9ea;display:flex;align-items:center;justify-content:center}
.stat strong{display:block;font-weight:800;font-size:34px;margin-top:14px;color:#222}
.stat span{display:block;font-size:13px;color:var(--grey);margin-top:2px}

/* projects */
.projects-bg{position:absolute;left:0;top:2905px;width:1200px;height:620px;background:radial-gradient(ellipse at 50% 40%,#eef1f5 0%,#ffffff 70%)}
.project{position:absolute;top:3056px;width:277px;text-align:center}
.project-photo{width:277px;height:187px}
.project p{font-size:12px;line-height:19px;color:var(--grey);margin-top:34px}

/* contact */
.contact-head{position:absolute;left:0;top:3470px;width:1200px;text-align:center}
.contact-head p{font-size:15px;line-height:21px;color:#333;margin-top:12px}
.field{position:absolute;background:var(--field);font-size:12px;color:#555;padding:8px 15px}
.submit{position:absolute;left:546px;top:3793px;width:109px;height:37px;border-radius:19px;background:var(--blue);color:var(--white);font-size:12px;font-weight:600;display:flex;align-items:center;justify-content:center}

/* footer */
.site-footer{position:absolute;left:0;top:3872px;width:1200px;height:405px;background:var(--navy-deep);color:var(--white)}
.foot-brand{position:absolute;left:150px;top:70px;display:flex;align-items:center;gap:10px}
.foot-brand .brand-dot{width:60px;height:60px;background:var(--white)}
.foot-brand .brand-name{color:var(--white);font-size:22px}
.foot-brand .brand-name small{font-size:10px}
.foot-contact{position:absolute;left:150px;font-size:13px;display:flex;gap:12px;align-items:flex-start;line-height:18px}
.foot-col{position:absolute;top:86px}
.foot-col h4{font-size:13px;font-weight:700;margin-bottom:14px}
.foot-col li{list-style:none;font-size:12px;line-height:25.5px;padding-left:16px;position:relative}
.foot-col li:before{content:"›";position:absolute;left:0;color:var(--blue-light)}
.subscribe{position:absolute;left:742px;top:116px;width:308px;height:36px;display:flex}
.subscribe span{flex:1;background:var(--white);border-radius:18px 0 0 18px;color:#666;font-size:12px;padding:11px 22px}
.subscribe b{width:104px;background:var(--blue);border-radius:0 18px 18px 0;font-size:14px;font-weight:500;display:flex;align-items:center;justify-content:center}
.social{position:absolute;top:232px;width:34px;height:34px;border-radius:50%;background:var(--blue)}
.foot-bar{position:absolute;left:0;top:326px;width:1200px;border-top:1px solid rgba(255,255,255,.12)}
.foot-legal{position:absolute;top:357px;font-size:11px;color:#d5dbe6}
</style>
</head>
<body>

<header class="site-header">
  <a class="brand" href="#"><span class="brand-dot"></span><span class="brand-name">K7R<small>CONSULTING ENGINEERS</small></span></a>
  <nav class="main-nav"><a>HOME</a><a>ABOUT US</a><a>SERVICES</a><a>MARKETS</a><a>PROJECTS</a></nav>
  <a class="nav-cta">CONTACT US</a>
</header>

<section class="hero">
  <div class="hero-photo" role="img" aria-label="Dusk skyline of high-rise city towers"></div>
  <div class="hero-feature" role="img" aria-label="Framed view looking up at a glass skyscraper"></div>
  <div class="hero-kicker">Consulting Engineers</div>
  <h1 class="hero-title">Building</h1>
  <div class="hero-sub">Management System</div>
  <a class="hero-btn">LEARN MORE <i></i></a>
  <div class="scroll-mouse"></div>
  <svg class="hero-bands" width="1200" height="730" viewBox="0 0 1200 730">
    <polygon points="240,735 240,700 1200,560 1200,600 1000,640 1200,700 1200,735" fill="#6fa9db"/>
    <polygon points="890,645 1200,600 1200,735" fill="#0b5cab"/>
    <polygon points="0,730 0,735 1200,735 1200,730" fill="#f5f7fb"/>
  </svg>
</section>

<section class="about">
  <div class="about-visual" role="img" aria-label="Glass office towers against a blue sky"></div>
  <div class="about-copy">
    <h2 class="section-title">About Our <b>Company</b></h2>
    <p class="first">Lorem ipsum dolor sit amet, consectetur adipiscing elit. Integer pulvinar, dui sit amet porttitor mollis,</p>
    <p>urna purus iaculis felis, eu convallis mi erat non ante. Curabitur vulputate scelerisque quam et laoreet. Vestibulum lacinia auctor mollis.</p>
    <p>Proin ac risus nec nibh commodo cursus. Morbi id mauris vel magna lacinia iaculis. Sed pellentesque arcu sit amet urna eleifend rhoncus. Integer pellentesque et justo vel imperdiet. Fusce porta libero ligula.</p>
    <a class="text-link">LEARN MORE</a>
  </div>
</section>

<div class="connector" style="top:1345px;height:63px"></div>

<article class="intro-card" style="left:150px">
  <div class="card-photo" role="img" aria-label="Colleagues reviewing work at a laptop" style="background:linear-gradient(135deg,#5b6a78,#a89a8c)"></div>
  <div class="card-badge"></div>
  <h3>Who we are</h3>
  <p>Lorem ipsum dolor sit consectetur<br>adipiscing elit integer pulvinar.</p>
  <a class="pill-btn">LEARN MORE</a>
</article>
<article class="intro-card" style="left:461px">
  <div class="card-photo" role="img" aria-label="Team gathered around a table planning" style="background:linear-gradient(135deg,#6b7f9a,#c2b2a0)"></div>
  <div class="card-badge"></div>
  <h3>What we do</h3>
  <p>Lorem ipsum dolor sit consectetur<br>adipiscing elit integer pulvinar.</p>
  <a class="pill-btn">LEARN MORE</a>
</article>
<article class="intro-card" style="left:772px">
  <div class="card-photo" role="img" aria-label="Overhead view of a team meeting with devices on a wooden desk" style="background:linear-gradient(135deg,#7d5a3f,#4c5866)"></div>
  <div class="card-badge"></div>
  <h3>How we do it</h3>
  <p>Lorem ipsum dolor sit consectetur<br>adipiscing elit integer pulvinar.</p>
  <a class="pill-btn">LEARN MORE</a>
</article>

<section class="services" role="img" aria-label="Server room corridor in deep blue tones"></section>
<svg class="abs" style="left:0;top:1880px" width="1200" height="170" viewBox="0 0 1200 170">
  <polygon points="0,0 1200,0 1200,0 955,0 0,0" fill="#fff"/>
  <polygon points="0,0 0,170 1200,170 1200,0 955,0 955,18 0,170" fill="none"/>
  <polygon points="0,-2 1200,-2 1200,2 955,10 0,130" fill="#fff"/>
  <polygon points="0,0 300,85 0,110" fill="#0b5cab"/>
  <polygon points="0,110 955,0 955,25 0,168" fill="#6fa9db"/>
  <polygon points="0,168 955,25 1200,0 1200,170" fill="#0c3f78"/>
</svg>
<h2 class="services-title">What <b>We Do</b></h2>
<p class="services-lede">Lorem ipsum dolor sit consectetur adipiscing elit integer.</p>
<div class="service-hub" role="img" aria-label="Framed city skyline seen from above"></div>
<svg class="abs" style="left:0;top:2200px" width="1200" height="320" viewBox="0 0 1200 320" fill="none" stroke="#fff" stroke-width="1.3">
  <polyline points="400,34 470,34 505,69"/><circle cx="505" cy="69" r="4" fill="#fff"/>
  <polyline points="415,155 468,155"/><circle cx="468" cy="155" r="4" fill="#fff"/>
  <polyline points="390,282 460,282 494,248"/><circle cx="494" cy="248" r="4" fill="#fff"/>
  <polyline points="820,34 750,34 716,69"/><circle cx="716" cy="69" r="4" fill="#fff"/>
  <polyline points="808,155 752,155"/><circle cx="752" cy="155" r="4" fill="#fff"/>
  <polyline points="828,282 760,282 726,248"/><circle cx="726" cy="248" r="4" fill="#fff"/>
</svg>
<div class="service-item" style="left:227px;top:2218px">Gap Analysis</div>
<div class="service-item" style="left:201px;top:2338px">Concept Design</div>
<div class="service-item" style="left:209px;top:2465px">Specification</div>
<div class="service-item" style="left:832px;top:2218px">Tender</div>
<div class="service-item" style="left:817px;top:2338px">Construction</div>
<div class="service-item" style="left:847px;top:2465px">DLP Tuning</div>

<div class="stat" style="left:142px">
  <div class="stat-ring"><svg width="30" height="30" viewBox="0 0 30 30" fill="none" stroke="#0b5cab" stroke-width="2"><path d="M5 14h5v12H5zM10 25h11l4-9v-3h-8l1-6-3-1-5 8"/></svg></div>
  <strong>20+</strong><span>Years of Experience</span>
</div>
<div class="stat" style="left:365px">
  <div class="stat-ring"><svg width="32" height="24" viewBox="0 0 32 24" fill="none" stroke="#0b5cab" stroke-width="2.4"><path d="M2 13l6 6L20 5M12 17l2 2L28 5"/></svg></div>
  <strong>300+</strong><span>Projects Completed</span>
</div>
<div class="stat" style="left:614px">
  <div class="stat-ring"><svg width="32" height="28" viewBox="0 0 32 28" fill="none" stroke="#0b5cab" stroke-width="1.8"><circle cx="16" cy="6" r="3.5"/><circle cx="9" cy="15" r="3"/><circle cx="23" cy="15" r="3"/><path d="M3 26c0-4 3-6 6-6s6 2 6 6M17 26c0-4 3-6 6-6s6 2 6 6"/></svg></div>
  <strong>25+</strong><span>Qualified Team Member</span>
</div>
<div class="stat" style="left:862px">
  <div class="stat-ring"><svg width="20" height="30" viewBox="0 0 20 30" fill="none" stroke="#0b5cab" stroke-width="2.4"><path d="M10 2v26M16 8c-1-2-3-3-6-3s-6 2-6 5 3 4 6 5 6 2 6 5-3 5-6 5-5-1-6-3"/></svg></div>
  <strong>$20M</strong><span>Annual Revenue</span>
</div>

<div class="projects-bg" role="img" aria-label="Faint floating city island backdrop"></div>
<div class="connector" style="top:2893px;height:63px"></div>
<h2 class="section-title abs" style="left:0;top:2972px;width:1200px;text-align:center;font-size:40px">Our <b>&nbsp;Projects</b></h2>
<article class="project" style="left:160px">
  <div class="project-photo" role="img" aria-label="Modern office campus at twilight" style="background:linear-gradient(180deg,#5f87b8,#2f4d6e 70%,#3c5b48)"></div>
  <p>Lorem ipsum dolor sit consectetur<br>adipiscing elit integer pulvinar.</p>
</article>
<article class="project" style="left:471px">
  <div class="project-photo" role="img" aria-label="Steel and glass walkway structure in warm light" style="background:linear-gradient(135deg,#d2a84a,#6a8aa0 55%,#2e4f73)"></div>
  <p>Lorem ipsum dolor sit consectetur<br>adipiscing elit integer pulvinar.</p>
</article>
<article class="project" style="left:782px">
  <div class="project-photo" role="img" aria-label="Glass tower facades seen from below" style="background:linear-gradient(135deg,#0f2a57,#2d5e9c 60%,#c7d6ea)"></div>
  <p>Lorem ipsum dolor sit consectetur<br>adipiscing elit integer pulvinar.</p>
</article>

<section class="contact-head">
  <h2 class="section-title" style="font-size:40px">Contact <b>Us</b></h2>
  <p>To contact the Northvale group please email us or<br>use the contact form below.</p>
</section>
<div class="field" style="left:377px;top:3592px;width:222px;height:31px">Name</div>
<div class="field" style="left:605px;top:3592px;width:223px;height:31px">Email</div>
<div class="field" style="left:377px;top:3630px;width:222px;height:31px">Phone</div>
<div class="field" style="left:605px;top:3630px;width:223px;height:31px">Subject</div>
<div class="field" style="left:377px;top:3668px;width:451px;height:111px">Message</div>
<a class="submit">SUBMIT</a>

<footer class="site-footer">
  <div class="foot-brand"><span class="brand-dot"></span><span class="brand-name">K7R<small>CONSULTING ENGINEERS</small></span></div>
  <div class="foot-contact" style="top:170px">
    <svg width="14" height="18" viewBox="0 0 14 18"><path d="M7 1a6 6 0 0 0-6 6c0 4 6 10 6 10s6-6 6-10a6 6 0 0 0-6-6z" fill="#6fa9db"/><circle cx="7" cy="7" r="2.2" fill="#0c1b3a"/></svg>
    <span>48 Harbourline Road, Level 3<br>Sydney NSW 2000</span>
  </div>
  <div class="foot-contact" style="top:232px;font-size:15px">
    <svg width="16" height="16" viewBox="0 0 16 16"><path d="M3 1l3 3-2 2c1 2 3 4 5 5l2-2 3 3-2 3C7 15 1 9 1 3z" fill="#6fa9db"/></svg>
    <span>02 5550 1487</span>
  </div>
  <div class="foot-col" style="left:402px"><h4>COMPANY</h4><ul><li>Home</li><li>About</li><li>Services</li><li>Markets</li><li>Projects</li><li>Contact</li></ul></div>
  <div class="foot-col" style="left:572px"><h4>SERVICES</h4><ul><li>Services</li><li>Services</li><li>Services</li><li>Services</li><li>Services</li><li>Services</li></ul></div>
  <div class="foot-col" style="left:750px"><h4>SUBSCRIBE</h4></div>
  <div class="subscribe"><span>Email address</span><b>Subscribe</b></div>
  <div class="foot-col" style="left:750px;top:200px"><h4>FOLLOW US</h4></div>
  <a class="social" style="left:751px" aria-label="Professional network profile"></a>
  <a class="social" style="left:803px" aria-label="Photo sharing profile"></a>
  <div class="foot-bar"></div>
  <div class="foot-legal" style="left:150px">© K7R consulting engineers. All Rights Reserved.</div>
  <div class="foot-legal" style="left:887px">Privacy Policy &nbsp;|&nbsp; Terms of Use</div>
</footer>

</body>
</html>
```